Property Management company

We need a design for our company Maplecrest Elder Commons. We are complex of apartments that we manage and operate. We do like the colors green or blue

Industry/Entity Type

Property Management,

Requirements
Must have
• color
Nice to have
• maybe be able to use as a watermark

```html
<!DOCTYPE html>
<html lang="en">
<head>
<meta charset="utf-8">
<title>Maplecrest Elder Commons – Letterhead</title>
<link href="https://fonts.googleapis.com/css2?family=Open+Sans:wght@400;700&family=Arimo:wght@400&family=Pinyon+Script&display=swap" rel="stylesheet">
<style>
  :root {
    --backdrop: #e6e6e6;
    --paper: #f1f1f1;
    --ink: #222428;
    --body-ink: #3a3b3f;
    --accent: #7a7fbf;
    --navy: #121a2c;
    --navy-soft: #1d2740;
    --rule: #9a9a9a;
  }
  * { box-sizing: border-box; margin: 0; padding: 0; }
  html, body {
    width: 1200px; height: 1200px; overflow: hidden;
    background: var(--backdrop);
  }
  .letterhead {
    position: absolute;
    left: 190px; top: 20px;
    width: 820px; height: 1160px;
    background: var(--paper);
    overflow: hidden;
    font-family: "Open Sans", Arial, sans-serif;
    color: var(--body-ink);
  }
  .brand {
    position: absolute;
    left: 62px; top: 40px;
    width: 160px;
    text-align: center;
  }
  .brand-dot {
    display: block;
    width: 52px; height: 52px;
    margin: 0 auto 12px;
    border-radius: 50%;
    background: var(--accent);
  }
  .brand-name {
    font-family: "Open Sans", Arial, sans-serif;
    font-weight: 700;
    font-size: 13px;
    line-height: 15px;
    letter-spacing: 1.2px;
    color: var(--ink);
    text-transform: uppercase;
  }
  .contact {
    position: absolute;
    left: 533px; top: 52px;
    height: 91px;
    border-left: 1px solid var(--rule);
    padding-left: 18px;
    font-family: "Arimo", Arial, sans-serif;
    font-size: 13px;
    color: #111;
    line-height: 16.5px;
  }
  .contact-address { margin-bottom: 7px; }
  .contact-line { display: flex; align-items: center; gap: 8px; }
  .contact-line svg { width: 11px; height: 11px; flex: none; }
  .letter-body {
    position: absolute;
    left: 111px; top: 274px;
    width: 599px;
    font-size: 13.6px;
    line-height: 19.3px;
  }
  .salutation { margin-bottom: 19px; }
  .letter-body p.paragraph {
    text-align: justify;
    margin-bottom: 19.5px;
  }
  .closing { margin-top: 53px; }
  .signature {
    font-family: "Pinyon Script", cursive;
    font-size: 25px;
    color: #1a1a1a;
    margin-top: 4px;
    padding-left: 6px;
  }
  .footer-wave {
    position: absolute;
    left: 0; bottom: 0;
    width: 820px; height: 130px;
  }
</style>
</head>
<body>
  <main class="letterhead">
    <header>
      <div class="brand">
        <span class="brand-dot"></span>
        <div class="brand-name">Maplecrest<br>Elder Commons</div>
      </div>
      <address class="contact" style="font-style:normal">
        <div class="contact-address">2750 Linden Grove Rd, Suite 4,<br>Ashford, OH 44012</div>
        <div class="contact-line">
          <svg viewBox="0 0 12 12"><path d="M2.5 1.2l2 .2.7 2.3-1.2.9c.6 1.3 1.5 2.2 2.8 2.8l.9-1.2 2.3.7.2 2c-4.5.6-8.8-3.7-8.2-8.2z" fill="var(--accent)"/></svg>
          <span>(555) 318-2740</span>
        </div>
        <div class="contact-line">
          <svg viewBox="0 0 12 12"><rect x="1" y="3" width="10" height="6.5" fill="var(--accent)"/><path d="M1 3l5 3.6L11 3" fill="none" stroke="#fff" stroke-width="0.9"/></svg>
          <span>info@maplecrestcommons.com</span>
        </div>
        <div class="contact-line">
          <svg viewBox="0 0 12 12"><circle cx="6" cy="6" r="4.6" fill="none" stroke="var(--accent)" stroke-width="1"/><ellipse cx="6" cy="6" rx="2" ry="4.6" fill="none" stroke="var(--accent)" stroke-width="0.8"/><path d="M1.4 6h9.2" stroke="var(--accent)" stroke-width="0.8"/></svg>
          <span>www.maplecrestcommons.com</span>
        </div>
      </address>
    </header>

    <section class="letter-body">
      <p class="salutation">Dear Daniel Harrow,</p>
      <p class="paragraph">Lorem ipsum dolor sit amet, consectetuer adipiscing elit, sed diam nonummy nibh euismod tincidunt ut laoreet dolore magna aliquam erat volutpat. Ut wisi enim ad minim veniam, quis nostrud exerci tation ullamcorper suscipit lobortis nisl ut aliquip ex ea commodo consequat. Duis dolore te feugait nulla facilisi. Nam liber tempor cum soluta nobis eleifend option congue nihil imperdiet doming id quod mazim placerat facer possim assum. Lorem ipsum dolor sit amet, consectetuer adipiscing elit, sed diam nonummy nibh euismod tincidunt ut laoreet dolore magna aliquam erat volutpat. Ut wisi enim ad minim veniam, quis nostrud exerci tation ullamcorper suscipit lobortis nisl ut aliquip ex ea commodo consequat.</p>
      <p class="paragraph">Consectetuer adipiscing elit, sed diam nonummy nibh euismod tincidunt ut laoreet dolore magna aliquam erat volutpat. Ut wisi enim ad minim veniam, quis nostrud exerci tation ullamcorper suscipit lobortis nisl ut aliquip ex ea commodo consequat. Consectetuer adipiscing elit, sed diam nonummy nibh euismod tincidunt ut laoreet dolore magna aliquam erat volutpat. Ut wisi enim ad minim veniam, quis nostrud exerci tation ullamcorper suscipit lobortis nisl ut aliquip ex ea commodo consequat.</p>
      <p class="paragraph">Consectetuer adipiscing elit, sed diam nonummy nibh euismod tincidunt ut laoreet dolore magna aliquam erat volutpat. Ut wisi enim ad minim veniam, quis nostrud exerci tation ullamcorper suscipit lobortis nisl ut aliquip ex ea commodo consequat. Consectetuer adipiscing elit, sed diam nonummy nibh euismod tincidunt ut laoreet dolore magna aliquam erat volutpat. Ut wisi enim ad minim veniam, quis nostrud exerci tation ullamcorper suscipit lobortis nisl ut aliquip ex ea commodo consequat.</p>
      <p class="closing">Sincerely Yours</p>
      <p class="signature">Thomas Whitfield</p>
    </section>

    <svg class="footer-wave" viewBox="0 0 820 130" preserveAspectRatio="none" aria-hidden="true">
      <path d="M0 96 Q 480 98 820 6 L820 28 Q 500 100 0 99 Z" fill="var(--accent)"/>
      <path d="M0 101 Q 520 104 820 35 L820 130 L0 130 Z" fill="var(--navy)"/>
      <path d="M260 115 Q 600 100 820 58 L820 80 Q 600 112 260 115 Z" fill="var(--navy-soft)" opacity="0.6"/>
    </svg>
  </main>
</body>
</html>
```